Software Application page - product section

I have developed a proposal generation application and want to improve the main user interface page.
This is the most important and most used page within my application and therefore it needs to look slick, clean, simple and easy to understand whilst looking very professional, creditable and established.
This is the page in which the user makes certain selections of products and the system will in turn display information on the product selected. The user can then add the product to the basket and the system also calculates the monthly cost of the product along with the profit the user makes by offering the particular product.
I have put something together myself and uploaded accordingly to give you an idea as to what it currently looks like and the structure that it needs to follow.
Section 1
This displays the Customer's account, proposal ID, Customer name etc
Section 2
I have these as radio buttons that the user selects, then clicks on the 'Search product' button. The items will then be displayed in section 3
Section 3
This datagrid displays the available products based on the section 2's selections
Section 4
shows information on the product that has been highlighed in section 3's datagrid. The user then clicks in qty field to enter the qty and then clicks the ADD shopping basket button to add the product to the basket in section 5 datagrid.
Section 5
This is the datagrid/shopping basket that displays all the products that the user has added.
Section 6
Displays all the figures including the total qtys', costs, revenue etc
WHILST IT IS IMPORTANT THAT THE DESIGN MUST FOLLOW THE STRUCTURE OF WHAT IS ATTACHED. I MUST POINT OUT THAT I AM NOT HAPPY WITH THE CURRENT DESIGN. I DO NOT LIKE THE LOOK AND FEEL OF THE CURRENT DESIGN AS IT LOOKS CHEAP AND AMATEURISH.
THE RADIO BUTTONS IN SECTION 1 FOR EXAMPLE SHOULD BE MORE CREATIVE, THE SIZE OF EACH SECTIONS CURRENTLY LOOK DISPROPORTIONATE. THE COLOURS ARE ALL OVER THE PLACE.
THE SIZE OF PAGE MUST BE 1009 X 689
PLEASE VISIT OUT OUR WEBSITE TO STICK TO THE COMPANIES BRAND: www.velantix.co.uk
I have other pages within my application that require designs along with icons and a lot of work on the website also require redesigning so the best design will also be given this work
Many thanks
Marcus

```html
<!DOCTYPE html>
<html lang="en">
<head>
<meta charset="utf-8">
<title>Velantix – Proposal Builder</title>
<link href="https://fonts.googleapis.com/css2?family=Arimo:wght@400;700&display=swap" rel="stylesheet">
<style>
:root{
  --bg:#e8c9ec;
  --card:#f8f8f8;
  --panel:#f0f0f0;
  --line:#e0e0e0;
  --plum:#7e5a8a;
  --plum-dark:#5e3a68;
  --plum-mid:#8a5e96;
  --orchid-top:#c592cf;
  --orchid-bot:#ab6eb8;
  --orchid-sel:#7e4f8d;
  --label:#8b5a9a;
  --text:#333;
  --fixed:#f9e4f6;
  --other:#cf8fd6;
  --scroll:#d9d9d9;
  --basket:#7a7a7a;
}
*{box-sizing:border-box;margin:0;padding:0}
html,body{width:1200px;height:1072px;overflow:hidden;background:var(--bg);font-family:"Arimo",Arial,sans-serif;color:var(--text)}
.stage{position:absolute;left:0;top:0;width:1120px;height:1000px;transform:scale(1.0714286);transform-origin:0 0}
.abs{position:absolute}
.app{left:55px;top:53px;width:1009px;height:897px;background:var(--card);box-shadow:0 2px 6px rgba(90,40,100,.15)}
/* nav */
.nav{left:55px;top:53px;width:1009px;height:52px;background:var(--plum);display:flex}
.brand{width:178px;background:#ececec;display:flex;align-items:center;gap:8px;padding-left:12px;font-size:27px;color:#555;letter-spacing:-.3px}
.brand-dot{width:30px;height:30px;border-radius:50%;background:var(--plum)}
.nav-tab{color:#fff;font-size:16px;display:flex;align-items:center;justify-content:center;border-right:1px solid #94729f}
.nav-tab.active{background:#fff;color:var(--plum);border-right:none}
/* panels */
.panel{background:var(--panel);border:1px solid var(--line)}
.info{left:75px;top:124px;width:464px;height:77px;font-size:14px}
.info span{position:absolute}
.lbl{color:var(--label)}
/* filters */
.filters{left:75px;top:222px;width:464px;height:326px}
.seg{position:absolute;left:18px;width:426px;height:32px;display:flex;border-radius:2px;background:linear-gradient(var(--orchid-top),var(--orchid-bot));border:1px solid #a468b1}
.seg span{color:#fff;font-size:14px;display:flex;align-items:center;justify-content:center;border-right:1px solid #9a5fa8}
.seg span.on{background:var(--orchid-sel)}
.rule{position:absolute;left:18px;width:426px;height:1px;background:#dcdcdc}
.search{left:75px;top:504px;width:413px;height:44px;background:#e4e4e4;font-size:14px;padding-left:24px;display:flex;align-items:center;color:#444}
.search-btn{left:488px;top:504px;width:51px;height:44px;background:var(--plum);display:flex;align-items:center;justify-content:center}
/* tables */
.thead{background:var(--plum);color:#fff;font-size:14px}
.tariff{left:75px;top:566px;width:464px;height:354px;background:#fff;border:1px solid var(--line)}
.trow{position:absolute;left:0;width:441px;height:32px;font-size:14px;border-bottom:1px solid #fff;background:#f2f2f2}
.trow span{position:absolute;top:8px}
.vscroll{background:#fff}
.hscroll{background:#f5f5f5}
.thumb{background:var(--scroll)}
/* product details */
.details{left:580px;top:124px;width:464px;height:222px}
.field{position:absolute;background:#fff;border:1px solid var(--line);font-size:14px;padding:11px 10px}
.icon-btn{position:absolute;top:300px;width:50px;height:36px;display:flex;align-items:center;justify-content:center;box-shadow:0 2px 0 rgba(0,0,0,.2)}
.basket{left:580px;top:367px;width:464px;height:163px;background:#f2f2f2;border:1px solid var(--line)}
.btn{position:absolute;display:flex;align-items:center;justify-content:center;color:#fff;box-shadow:0 2px 0 rgba(0,0,0,.2)}
/* summary */
.summary{left:580px;top:593px;width:464px;height:270px;background:#f2f2f2;border:1px solid var(--line);font-size:14px}
.srow{position:absolute;left:0;width:464px;height:32px}
.srow span{position:absolute;top:8px}
.num{width:60px;text-align:center}
</style>
</head>
<body>
<div class="stage">
  <div class="abs app"></div>

  <header class="abs nav">
    <div class="brand"><span class="brand-dot"></span>Velantix</div>
    <div class="nav-tab active" style="width:105px">Home</div>
    <div class="nav-tab" style="width:86px">Task</div>
    <div class="nav-tab" style="width:113px">Reports</div>
    <div class="nav-tab" style="width:113px">Contact</div>
    <div class="nav-tab" style="width:105px">Setting</div>
  </header>

  <!-- Section 1 -->
  <section class="abs panel info">
    <span class="lbl" style="left:23px;top:14px">Proposal Id&nbsp; :</span>
    <span style="left:117px;top:14px">1334235</span>
    <span class="lbl" style="left:231px;top:14px">Customer Id</span>
    <span style="left:346px;top:14px">:&nbsp;&nbsp;110399</span>
    <span class="lbl" style="left:23px;top:44px">Status</span>
    <span style="left:104px;top:44px">:&nbsp; Incomplete</span>
    <span class="lbl" style="left:231px;top:44px">Customer Name</span>
    <span style="left:346px;top:44px">:&nbsp;&nbsp;Velantix Ltd</span>
  </section>

  <!-- Section 2 -->
  <section class="abs panel filters">
    <div class="seg" style="top:17px"><span class="on" style="width:77px">Mobile</span><span style="width:101px">Fixed Line</span><span style="width:132px">Other Products</span></div>
    <div class="rule" style="top:60px"></div>
    <div class="seg" style="top:70px"><span style="width:54px">K4</span><span style="width:96px">Vertafon</span><span style="width:53px">ZX</span><span style="width:84px">Amberly</span></div>
    <div class="rule" style="top:112px"></div>
    <div class="seg" style="top:122px"><span style="width:64px">New</span><span style="width:79px">Resign</span></div>
    <div class="rule" style="top:164px"></div>
    <div class="seg" style="top:174px"><span style="width:51px">12</span><span style="width:51px">24</span><span style="width:53px">36</span><span style="width:52px">48</span><span style="width:51px">60</span><span style="width:70px">Other</span></div>
    <div class="rule" style="top:216px"></div>
    <div class="seg" style="top:226px"><span style="width:102px">Share Plan</span><span style="width:108px">Single Plan</span><span style="width:69px">MBB</span><span style="width:80px">Add-On</span></div>
    <div class="rule" style="top:268px"></div>
  </section>
  <div class="abs search">Search Product...</div>
  <div class="abs search-btn">
    <svg width="24" height="24" viewBox="0 0 24 24" fill="none" stroke="#fff" stroke-width="2.6"><circle cx="10" cy="10" r="7"/><line x1="15" y1="15" x2="21" y2="21" stroke-linecap="round"/></svg>
  </div>

  <!-- Section 3 -->
  <section class="abs tariff">
    <div class="abs thead" style="left:0;top:0;width:462px;height:44px">
      <span class="abs" style="left:23px;top:15px">TARRIF</span>
      <span class="abs" style="left:297px;top:0;width:1px;height:44px;background:#fff"></span>
      <span class="abs" style="left:354px;top:15px">PRICE</span>
    </div>
    <div class="trow" style="top:44px"><span style="left:24px">Business Single 300</span><span style="left:327px">19.03</span></div>
    <div class="trow" style="top:76px"><span style="left:24px">Business Single 600</span><span style="left:327px">25.03</span></div>
    <div class="trow" style="top:108px"><span style="left:24px">Business Single 900</span><span style="left:327px">19.03</span></div>
    <div class="trow" style="top:140px"><span style="left:24px">Business Single 1200</span><span style="left:327px">25.03</span></div>
    <div class="trow" style="top:172px"><span style="left:24px">Business Single 300</span><span style="left:327px">19.03</span></div>
    <div class="trow" style="top:204px"><span style="left:24px">Business Single 600</span><span style="left:327px">25.03</span></div>
    <div class="trow" style="top:236px"><span style="left:24px">Business Single 900</span><span style="left:327px">19.03</span></div>
    <div class="trow" style="top:268px"><span style="left:24px">Business Single 1200</span><span style="left:327px">25.03</span></div>
    <div class="trow" style="top:300px;height:31px"><span style="left:24px">Business Single 1200</span><span style="left:327px">25.03</span></div>
    <div class="abs" style="left:297px;top:44px;width:1px;height:287px;background:#e2e2e2"></div>
    <div class="abs vscroll" style="left:441px;top:44px;width:21px;height:287px">
      <div class="abs thumb" style="left:0;top:34px;width:21px;height:78px"></div>
    </div>
    <div class="abs hscroll" style="left:0;top:331px;width:462px;height:21px">
      <div class="abs thumb" style="left:37px;top:0;width:110px;height:21px"></div>
    </div>
  </section>

  <!-- Section 4 -->
  <section class="abs panel details">
    <div class="field" style="left:14px;top:15px;width:175px;height:37px">Product</div>
    <div class="field" style="left:201px;top:15px;width:112px;height:37px">Qty</div>
    <div class="field" style="left:325px;top:15px;width:124px;height:37px">Total Cost</div>
    <div class="field" style="left:14px;top:62px;width:175px;height:37px">Reveneu %</div>
    <div class="field" style="left:201px;top:62px;width:112px;height:37px">Minutes</div>
    <div class="field" style="left:325px;top:62px;width:124px;height:37px">Texts</div>
    <div class="field" style="left:14px;top:108px;width:435px;height:56px">Data</div>
  </section>
  <div class="icon-btn" style="left:758px;background:var(--plum)">
    <svg width="12" height="24" viewBox="0 0 12 24" fill="#fff"><circle cx="6" cy="3.5" r="3"/><path d="M1 9h8v11h2.5v3H.5v-3H3v-8H1z"/></svg>
  </div>
  <div class="icon-btn" style="left:817px;background:var(--basket)">
    <svg width="26" height="22" viewBox="0 0 26 22" fill="none" stroke="#fff" stroke-width="2"><path d="M8 8l5-6 5 6"/><path d="M1 8h24l-3 12H4z"/><line x1="9" y1="11" x2="9" y2="17"/><line x1="13" y1="11" x2="13" y2="17"/><line x1="17" y1="11" x2="17" y2="17"/></svg>
  </div>

  <!-- Section 5 -->
  <section class="abs basket">
    <div class="abs thead" style="left:0;top:0;width:462px;height:44px">
      <span class="abs" style="left:23px;top:15px">PRODUCT</span>
      <svg class="abs" style="left:159px;top:17px" width="7" height="11" viewBox="0 0 7 11" fill="#fff"><path d="M3.5 0L7 4H0zM0 7h7l-3.5 4z"/></svg>
      <span class="abs" style="left:178px;top:15px">TYPE</span>
      <span class="abs" style="left:268px;top:15px">PRICE</span>
      <span class="abs" style="left:345px;top:15px">QTY</span>
      <span class="abs" style="left:408px;top:15px">TOTAL</span>
    </div>
    <div class="abs" style="left:0;top:75px;width:440px;height:1px;background:#fff"></div>
    <div class="abs" style="left:0;top:107px;width:440px;height:1px;background:#fff"></div>
    <div class="abs" style="left:177px;top:0;width:1px;height:139px;background:#e0e0e0"></div>
    <div class="abs" style="left:247px;top:0;width:1px;height:139px;background:#e0e0e0"></div>
    <div class="abs" style="left:328px;top:0;width:1px;height:139px;background:#e0e0e0"></div>
    <div class="abs" style="left:392px;top:0;width:1px;height:139px;background:#e0e0e0"></div>
    <div class="abs vscroll" style="left:440px;top:44px;width:22px;height:95px">
      <div class="abs thumb" style="left:0;top:30px;width:22px;height:24px"></div>
    </div>
    <div class="abs hscroll" style="left:0;top:139px;width:462px;height:22px;background:#fff">
      <div class="abs thumb" style="left:37px;top:0;width:110px;height:22px"></div>
    </div>
  </section>
  <div class="btn" style="left:968px;top:541px;width:75px;height:31px;background:var(--plum);font-size:14px;font-weight:700">DELETE</div>

  <!-- Section 6 -->
  <section class="abs summary">
    <div class="abs thead" style="left:0;top:0;width:462px;height:44px;font-weight:700;font-size:13px;line-height:15px">
      <span class="abs num" style="left:199px;top:15px">QTY</span>
      <span class="abs" style="left:276px;top:7px;width:74px;text-align:center">MOTHLY<br>COST</span>
      <span class="abs" style="left:368px;top:7px;width:80px;text-align:center">MOTHLY<br>REVENUE</span>
    </div>
    <div class="srow" style="top:44px"><span style="left:18px">Mobile Voice</span><span class="num" style="left:199px">0</span><span class="num" style="left:282px">0</span><span class="num" style="left:377px">0</span></div>
    <div class="srow" style="top:76px"><span style="left:18px">Mobile Data Only</span><span class="num" style="left:199px">0</span><span class="num" style="left:282px">0</span><span class="num" style="left:377px">0</span></div>
    <div class="srow" style="top:108px;font-weight:700"><span style="left:18px">Mobile Total</span><span class="num" style="left:199px">0</span><span class="num" style="left:282px">0</span><span class="num" style="left:377px">0</span></div>
    <div class="srow" style="top:140px;background:var(--fixed);font-weight:700"><span style="left:18px">Fixed Line</span><span class="num" style="left:199px">-</span><span class="num" style="left:282px">0</span><span class="num" style="left:377px">0</span></div>
    <div class="srow" style="top:172px;background:var(--other);color:#fff;font-weight:700"><span style="left:18px">Other Products</span><span class="num" style="left:199px">-</span><span class="num" style="left:282px">0</span><span class="num" style="left:377px">0</span></div>
    <div class="srow" style="top:204px;height:64px;background:var(--plum);color:#fff;font-weight:700">
      <span style="left:18px;top:13px">Total Monthly Cost</span><span class="num" style="left:199px;top:13px;font-weight:400">-</span><span class="num" style="left:282px;top:13px">0</span><span class="num" style="left:377px;top:13px;font-weight:400">-</span>
      <span style="left:18px;top:38px">Total Monthly Revenue</span><span class="num" style="left:199px;top:38px;font-weight:400">-</span><span class="num" style="left:282px;top:38px;font-weight:400">-</span><span class="num" style="left:377px;top:38px">999999</span>
    </div>
  </section>

  <div class="btn" style="left:903px;top:880px;width:65px;height:39px;background:var(--plum-mid)">
    <svg width="30" height="20" viewBox="0 0 30 20" fill="#fff"><path d="M0 10L12 0v6h18v8H12v6z"/></svg>
  </div>
  <div class="btn" style="left:979px;top:880px;width:65px;height:39px;background:var(--plum-dark)">
    <svg width="30" height="20" viewBox="0 0 30 20" fill="#fff"><path d="M30 10L18 0v6H0v8h18v6z"/></svg>
  </div>
</div>
</body>
</html>
```